Card for invoking rights with police

Our criminal defense law firm is seeking proposals for a design for our card intended for clients to carry with them in their car. Upon being pulled over, they would hand this card to the officer.
Text for the back of the card:
"For Law Enforcement:"
"I will comply with lawful orders but respectfully decline any test or other requests without my attorney. I wish to remain silent, do not consent to searches, and request to speak with my attorney now.
The back of the card should prominently feature the text and the firm logo should be secondary.
Front
Must prominently feature contact info: 503-555-0182. Do not include attorney name, email, phone from the example file. This is intended to be generic for the firm and not tied to an individual lawyer.
Included for design reference: current business card, firm logo.
We intend to use trenvo.com to produce the cards.
Updates
The back of the card should prominently display the text regarding invocation of rights. Please title it "For Law Enforcement".
Target Market(s)
People who have been stopped by police
Contact Information for Business Card
see project description
Look and feel

```html
<!DOCTYPE html>
<html lang="en">
<head>
<meta charset="utf-8">
<title>Harlow Law Firm – Rights Card</title>
<link href="https://fonts.googleapis.com/css2?family=Lato:wght@400;700;900&display=swap" rel="stylesheet">
<style>
  :root{
    --navy:#063256;
    --navy-deep:#04294a;
    --stone:#b9bcc0;
    --ink:#444a52;
    --paper:#ffffff;
    --backdrop:#3a3d42;
  }
  *{box-sizing:border-box;margin:0;padding:0}
  html,body{width:1200px;height:952px;overflow:hidden}
  body{
    background:var(--backdrop);
    font-family:"Lato",sans-serif;
    display:flex;align-items:center;justify-content:center;gap:40px;
  }
  .card{
    position:relative;width:540px;height:310px;border-radius:22px;overflow:hidden;
    box-shadow:0 14px 30px rgba(0,0,0,.35);
  }
  .card-corner{position:absolute;left:0;bottom:0}

  /* back: rights statement */
  .card--back{background:var(--navy);color:var(--paper);text-align:center}
  .card--back .card-corner path{fill:var(--stone)}
  .firm-mark{
    position:absolute;top:34px;left:0;right:0;
    display:flex;align-items:center;justify-content:center;gap:12px;
  }
  .firm-mark__square{width:30px;height:30px}
  .firm-name{font-weight:400;letter-spacing:.22em;font-size:24px;text-transform:uppercase}
  .card--back .firm-mark__square{background:var(--stone)}
  .card--back .firm-name{color:var(--paper)}
  .rights-title{
    position:absolute;top:112px;left:70px;right:70px;
    display:flex;align-items:center;gap:14px;font-weight:700;font-size:20px;
  }
  .rights-title::before,.rights-title::after{content:"";flex:1;height:1px;background:var(--stone)}
  .rights-text{
    position:absolute;top:156px;left:60px;right:60px;
    font-size:14.5px;line-height:1.5;color:#e4e7ea;
  }

  /* front: contact */
  .card--front{background:var(--paper)}
  .card--front .card-corner path{fill:var(--navy)}
  .card--front .firm-mark{top:46px;left:40px;right:auto;justify-content:flex-start}
  .card--front .firm-mark__square{background:var(--navy)}
  .card--front .firm-name{color:var(--navy);font-size:20px}
  .contact{
    position:absolute;right:36px;top:118px;text-align:right;color:var(--ink);
  }
  .contact__role{font-size:17px;color:var(--navy);font-weight:700;letter-spacing:.04em;text-transform:uppercase}
  .contact__rule{width:70px;height:2px;background:var(--ink);margin:8px 0 12px auto}
  .contact__list{list-style:none;font-size:14px;line-height:1.35}
  .contact__list li{display:flex;justify-content:flex-end;align-items:center;gap:10px;margin-bottom:6px}
  .contact__list .contact__phone{font-size:20px;font-weight:900;color:var(--navy)}
  .icon{width:20px;height:20px;border-radius:4px;background:var(--navy);flex:none;display:flex;align-items:center;justify-content:center}
  .icon svg{width:13px;height:13px;fill:var(--paper)}
</style>
</head>
<body>

  <section class="card card--back" aria-label="Card back">
    <svg class="card-corner" width="80" height="120" viewBox="0 0 80 120"><path d="M0 0 L40 40 L40 120 L0 120 Z"/></svg>
    <div class="firm-mark">
      <span class="firm-mark__square"></span>
      <span class="firm-name">Harlow Law Firm</span>
    </div>
    <h2 class="rights-title">For Law Enforcement</h2>
    <p class="rights-text">I will comply with lawful orders but respectfully decline any test or other requests without my attorney. I wish to remain silent, do not consent to searches, and request to speak with my attorney now.</p>
  </section>

  <section class="card card--front" aria-label="Card front">
    <svg class="card-corner" width="300" height="90" viewBox="0 0 300 90"><path d="M0 0 L250 0 L300 90 L0 90 Z" transform="translate(0,0)" opacity="0"/><path d="M0 90 L0 40 L230 40 L270 90 Z"/></svg>
    <div class="firm-mark">
      <span class="firm-mark__square"></span>
      <span class="firm-name">Harlow Law Firm</span>
    </div>
    <div class="contact">
      <p class="contact__role">Criminal Defense</p>
      <div class="contact__rule"></div>
      <ul class="contact__list">
        <li><span>2215 Alder Crest Way, Suite 300<br>Lakeview, WA 98041</span>
          <span class="icon"><svg viewBox="0 0 24 24"><path d="M12 2a7 7 0 0 0-7 7c0 5 7 13 7 13s7-8 7-13a7 7 0 0 0-7-7zm0 9.5A2.5 2.5 0 1 1 12 6.5a2.5 2.5 0 0 1 0 5z"/></svg></span></li>
        <li><span class="contact__phone">503-555-0182</span>
          <span class="icon"><svg viewBox="0 0 24 24"><path d="M6.6 10.8a15 15 0 0 0 6.6 6.6l2.2-2.2a1 1 0 0 1 1-.25 11.4 11.4 0 0 0 3.6.57 1 1 0 0 1 1 1V20a1 1 0 0 1-1 1A17 17 0 0 1 3 4a1 1 0 0 1 1-1h3.5a1 1 0 0 1 1 1c0 1.25.2 2.45.57 3.57a1 1 0 0 1-.25 1z"/></svg></span></li>
        <li><span>office@harlowlawfirm.com</span>
          <span class="icon"><svg viewBox="0 0 24 24"><path d="M3 5h18v14H3zm2 2v.5l7 4.5 7-4.5V7zm0 2.9V17h14V9.9l-7 4.5z"/></svg></span></li>
        <li><span>www.harlowlawfirm.com</span>
          <span class="icon"><svg viewBox="0 0 24 24"><path d="M5 3l14 8-6 1.5L16 20l-2.5 1-3-7.2L6 18z"/></svg></span></li>
      </ul>
    </div>
  </section>

</body>
</html>
```